Business Card Design for Massage Therapist

*I am a qualified massage therapist & require a business card for my new business 'Tidal Touch & Wellness'.
*Contact details I'd like included on the card are: Elise Brantry, Mobile: 0481562930, Email: tidaltw@mailvane.com
*It is a massage business dedicated to providing quality therapeutic massage treatments, that will later incorporate natural therapies.
* Styles Include: Swedish, Relaxation, Pregnancy, Deep Tissue & Sports Massage
*I offer the styles of massage as listed above & a mobile service that allows clients to book a massage in the comfort of their own home.
*I'd like my logo to be fairly simple, streamlined, modern & reflect what my business services are - one people will easily remember.
*I'd like the colors to represent & emit a sense of calm, be fresh, welcoming, natural colors that appeal to a wide range of people.
*Colors I'd like to see are: pale blue, aqua & greens.

Target Market(s)

Both Male & Female, aged 20 to 65, singles, couples, parents, business people who are interested in their health, fitness & general wellbeing and maintenance. Located in the Harbourvale area and surrounding suburbs of Melbourne.

Industry/Entity Type

Massage

Requirements
Must have
• Fonts used in logos should be owned by the designer.
Should not have
• I don't want the design to have someone being massaged in it (pictures/photos) or have it look too clinical & sterile.

```html
<!DOCTYPE html>
<html lang="en">
<head>
<meta charset="utf-8">
<title>Tidal Touch &amp; Wellness – Business Card</title>
<link rel="stylesheet" href="https://fonts.googleapis.com/css2?family=Oxygen:wght@300;400&display=swap">
<style>
  :root {
    --page-bg: #eceeee;
    --card-bg: #ffffff;
    --aqua-deep: #9fe6df;
    --aqua-mid: #b9eee9;
    --aqua-pale: #dcf6f3;
    --ink-teal: #1f4a50;
    --text-light: #ffffff;
    --spa-coral: #f08a5d;
    --spa-cream: #f4f1ea;
  }
  * { margin: 0; padding: 0; box-sizing: border-box; }
  html, body {
    width: 1200px;
    height: 710px;
    overflow: hidden;
    background: var(--page-bg);
    font-family: "Oxygen", "Trebuchet MS", sans-serif;
  }
  .business-card {
    position: absolute;
    left: 80px;
    top: 35px;
    width: 1040px;
    height: 640px;
    background: var(--card-bg);
    overflow: hidden;
    box-shadow: 0 6px 18px rgba(0, 0, 0, 0.18);
  }
  .wave-shapes {
    position: absolute;
    inset: 0;
    width: 100%;
    height: 100%;
  }
  .business-name {
    position: absolute;
    left: 80px;
    top: 146px;
    font-size: 29px;
    font-weight: 400;
    color: var(--text-light);
    letter-spacing: 0.2px;
  }
  .styles-heading {
    position: absolute;
    left: 80px;
    top: 288px;
    font-size: 26px;
    font-weight: 300;
    color: var(--text-light);
    opacity: 0.85;
  }
  .styles-list {
    position: absolute;
    left: 78px;
    top: 340px;
    list-style: none;
    font-size: 25px;
    font-weight: 300;
    line-height: 38px;
    color: var(--text-light);
    opacity: 0.85;
  }
  .spa-still-life {
    position: absolute;
    left: 560px;
    top: 130px;
    width: 412px;
    height: 112px;
    border-radius: 56px;
    background: linear-gradient(90deg, rgba(240,138,93,0) 0%, var(--spa-coral) 25%, #e0643f 55%, var(--spa-cream) 78%, rgba(244,241,234,0.4) 100%);
  }
  .contact-block {
    position: absolute;
    right: 68px;
    text-align: right;
    color: var(--ink-teal);
  }
  .therapist-name {
    top: 298px;
    font-size: 48px;
    font-weight: 400;
  }
  .therapist-role {
    top: 370px;
    font-size: 28px;
    font-weight: 400;
  }
  .contact-line {
    font-size: 26px;
    font-weight: 400;
  }
  .contact-mobile { top: 474px; }
  .contact-email { top: 518px; }
</style>
</head>
<body>
  <section class="business-card">
    <svg class="wave-shapes" viewBox="0 0 1040 640" aria-hidden="true">
      <circle cx="560" cy="170" r="370" fill="var(--aqua-pale)"/>
      <circle cx="200" cy="250" r="470" fill="var(--aqua-mid)"/>
      <circle cx="180" cy="120" r="400" fill="var(--aqua-deep)" opacity="0.75"/>
    </svg>

    <h1 class="business-name">Tidal Touch &amp; Wellness</h1>

    <p class="styles-heading">Styles Include:</p>
    <ul class="styles-list">
      <li>Swedish</li>
      <li>Relaxation</li>
      <li>Pregnancy</li>
      <li>Deep Tissue</li>
      <li>Sports Massage</li>
    </ul>

    <div class="spa-still-life" role="img" aria-label="Photo of red orchid sprays beside rolled white towels and tea-light candles"></div>

    <p class="contact-block therapist-name">Elise Brantry</p>
    <p class="contact-block therapist-role">Massage Therapist</p>
    <p class="contact-block contact-line contact-mobile">Mobile: 0481562930</p>
    <p class="contact-block contact-line contact-email">Email: tidaltw@mailvane.com</p>
  </section>
</body>
</html>
```